Funeral Home needs a tri-fold brochure

We need to have a tri-fold brochure designed for our mortuary. The name of the mortuary is Willowmere Mortuary. The purpose of this brochure is to give consumers and decision makers an easy glimpse into our business.

The brochure will be tri-fold and have full color on both side.(8.5 x 11)

We are not what most people think in terms of a "traditional" funeral home. Do not use anything with a gothic feel. Our logo is light and simple which is how we would like this brochure to also be. The logo is attached. The colors we like are green, gold, white, and black.

Our mortuary offers affordable burial and cremation services. Some key points that we would like noted in brochure are family owned and operated, on-site cremation, and we service all religious faiths.

This is my first time requesting a brochure with ArtFolio, so I'm not sure if I should have text already written or not. I'm open to any questions or suggestions so don't be afraid to ask. I will answer as soon as possible.
Updates

I have just uploaded a scan of an old brochure that the business used that we don't want the new one to look anything like. Also I uploaded a sheet of copy for the features we would like shown on the brochure. Added Wednesday, September 10, 2014

Target Market(s)

decision influencers in churches, hospices, and hospitals. Also families that may be in need of our service.

Industry/Entity Type

Funeral Home

Font styles to use
Serif

Colors
acd036

Requirements
Must have
• My project must have our logo and be a bright brochure.
Should not have
• The project should not have a gothic feel, or use anything that is associated with "traditional" mortuaries like the dove or horse and carriage. No pictures of caskets, urns, or hearses. I have attached a picture of an older brochure that the business has. New design should not look anything like this one.

```html
<!DOCTYPE html>
<html lang="en">
<head>
<meta charset="utf-8">
<title>Willowmere Mortuary – Brochure Outside</title>
<link href="https://fonts.googleapis.com/css2?family=Questrial&family=Arimo:wght@700&display=swap" rel="stylesheet">
<style>
  :root {
    --green: #7dbb40;
    --green-mid: #88c23e;
    --lime: #aed136;
    --lime-light: #b2d538;
    --white: #ffffff;
    --ink: #151515;
  }
  html, body {
    margin: 0;
    padding: 0;
    overflow: hidden;
    background: var(--green);
  }
  .brochure {
    position: relative;
    width: 1200px;
    height: 927px;
    overflow: hidden;
    background: var(--green);
    font-family: "Questrial", sans-serif;
  }
  .center-band {
    position: absolute;
    left: 397px;
    top: 0;
    width: 409px;
    height: 927px;
    background: var(--lime);
  }
  .waves {
    position: absolute;
    inset: 0;
  }
  .panel {
    position: absolute;
    top: 118px;
    text-align: center;
  }
  .history {
    left: 5px;
    width: 400px;
    color: var(--white);
    font-size: 19.5px;
    line-height: 39.4px;
    letter-spacing: 0.2px;
  }
  .history h2 {
    margin: 0 0 -2px;
    font-family: "Arimo", sans-serif;
    font-weight: 700;
    font-size: 21px;
    line-height: 32px;
  }
  .history p { margin: 0; }
  .contact {
    left: 405px;
    width: 400px;
    color: var(--ink);
    font-size: 24px;
    line-height: 39.4px;
  }
  .contact h2 {
    margin: 0 0 -1px;
    font-weight: 400;
    font-size: 25px;
    line-height: 36px;
  }
  .contact p { margin: 0; }
  .brand-name {
    position: absolute;
    left: 840px;
    top: 186px;
    width: 330px;
    text-align: center;
    color: var(--ink);
    font-size: 28px;
    letter-spacing: 0.5px;
    margin: 0;
  }
</style>
</head>
<body>
<main class="brochure">
  <div class="center-band"></div>

  <svg class="waves" width="1200" height="927" viewBox="0 0 1200 927" aria-hidden="true">
    <defs>
      <linearGradient id="lowerGlow" x1="0" y1="0" x2="0" y2="1">
        <stop offset="0" stop-color="#8cc63d"/>
        <stop offset="1" stop-color="#a8d036"/>
      </linearGradient>
    </defs>
    <path d="M0,745 C400,700 650,650 800,530 C950,410 1080,350 1200,350 L1200,927 L0,927 Z" fill="var(--lime-light)"/>
    <path d="M0,758 C400,722 660,690 830,565 C965,465 1090,395 1200,388 L1200,927 L0,927 Z" fill="var(--green-mid)"/>
    <path d="M0,760 C300,770 500,800 700,790 C850,780 1000,790 1200,830 L1200,927 L0,927 Z" fill="url(#lowerGlow)"/>
    <path d="M0,872 C250,850 500,835 700,790 C850,755 1000,765 1200,845 L1200,927 L0,927 Z" fill="#a6cf37" opacity="0.8"/>
  </svg>

  <section class="panel history">
    <h2>History</h2>
    <p>Willowmere Mortuary was started in<br>
    2001 with the goal of providing an<br>
    affordable burial and cremation<br>
    service without cutting corners.<br>
    Now owned by father and son duo,<br>
    Walter and Daniel Hale, Willowmere<br>
    Mortuary is proud to be family<br>
    owned and operated and a leader<br>
    in the funeral industry.</p>
  </section>

  <section class="panel contact">
    <h2>Address and contact info</h2>
    <p>4120 W. Meadowlark Ave,<br>
    Sun Valley, AZ 85300<br>
    Phone: 623-555-0140<br>
    Fax: 623-555-0141<br>
    Web:<br>
    www.WillowmereMortuary.com<br>
    Email:<br>
    wecare@willowmeremortuary.com</p>
  </section>

  <p class="brand-name">WILLOWMERE MORTUARY</p>
</main>
</body>
</html>
```